Leuchtkasten für Pflegedienst
Zielgruppe
Wir sind ein ambulnter Pflegedienst in Rostock. Derzeit befindet sich am Haus ein runder Leuchtkasten mit dem alten Logo. Das Logo wurde erneuert. Nun soll der Leuchtkasten mit einem Durchmessr von 80 cm neu gestaltet werden.
Aufgabenstellung
bitte zwei unterscheideliche Entwürfe für die Vorder und die Rückseite. Es sollte auf der einen Seite vielleicht das Logo anthalten sein und auf der anderen Seite eine andere kreative Idee. Hauskrankenpflege Sorgenhaus Linde sollten enthalten sein, sowie die Telefonummer 0381-52946138
Auf der anderen Seite wurde ein Schriftzug in Edelstahl rostoptik montiert.
Wichtig ist, dass das der ENtwurf auf einer durchleichtbaren Folie gedruckt werden kann.
Der KAffee slogan war füe eine andere Aktion und sollte nicht auf den Leuchtkasten.

```html
<!DOCTYPE html>
<html lang="de">
<head>
<meta charset="utf-8">
<title>Leuchtkasten Sorgenhaus Linde – Vorder- und Rückseite</title>
<link rel="stylesheet" href="https://fonts.googleapis.com/css2?family=Damion&family=Kaushan+Script&family=Open+Sans:wght@700&family=Fira+Sans:ital,wght@0,600;1,600&display=swap">
<style>
  :root {
    --navy: #171d33;
    --blue: #2e7bb5;
    --teal: #5dbda6;
    --white: #ffffff;
    --outline: #1a1a1a;
  }
  html, body {
    margin: 0;
    padding: 0;
    width: 1200px;
    height: 1106px;
    overflow: hidden;
    background: var(--white);
  }
  .sign-sheet {
    width: 1200px;
    height: 1106px;
    display: flex;
    align-items: center;
    justify-content: space-around;
  }
  .sign-face {
    width: 560px;
    height: 560px;
    display: block;
  }
  .script-name { font-family: "Damion", cursive; fill: var(--white); }
  .script-place { font-family: "Kaushan Script", cursive; fill: var(--blue); }
  .phone { font-family: "Open Sans", sans-serif; font-weight: 700; fill: var(--white); }
  .mark-name-light { font-family: "Open Sans", sans-serif; font-weight: 700; fill: var(--white); }
  .ring-text { font-family: "Fira Sans", sans-serif; font-weight: 600; font-size: 54px; }
  .ring-text.blue { fill: var(--blue); }
  .ring-text.dark { fill: var(--navy); }
  .mark-name-blue { font-family: "Fira Sans", sans-serif; font-weight: 600; fill: var(--blue); }
</style>
</head>
<body>
<main class="sign-sheet">

  <!-- Vorderseite -->
  <svg class="sign-face sign-front" viewBox="0 0 820 820" role="img" aria-label="Vorderseite: Sorgenhaus Linde mit Telefonnummer">
    <defs>
      <clipPath id="front-clip"><circle cx="410" cy="410" r="410"/></clipPath>
    </defs>
    <g clip-path="url(#front-clip)">
      <rect class="front-bg" width="820" height="820" fill="var(--navy)"/>
      <path class="front-band" d="M0 455 C 200 590 450 695 820 680 L820 820 L0 820 Z" fill="var(--teal)"/>
    </g>

    <g class="front-mark">
      <circle cx="410" cy="190" r="135" fill="none" stroke="var(--white)" stroke-width="14"/>
      <text class="mark-name-light" x="410" y="182" text-anchor="middle" font-size="34">Sorgenhaus</text>
      <text class="mark-name-light" x="410" y="222" text-anchor="middle" font-size="34">Linde</text>
    </g>

    <text class="script-name" x="410" y="445" text-anchor="middle" font-size="118">Sorgenhaus</text>
    <text class="script-place" x="410" y="560" text-anchor="middle" font-size="112">Linde</text>

    <text class="phone" x="310" y="690" text-anchor="middle" font-size="58" transform="rotate(19 310 690)">0381-52946138</text>
  </svg>

  <!-- Rückseite -->
  <svg class="sign-face sign-back" viewBox="0 0 820 820" role="img" aria-label="Rückseite: Hauskrankenpflege im Kreis um Sorgenhaus Linde">
    <defs>
      <path id="ring-path" d="M 410 70 A 340 340 0 1 1 409.99 70 Z"/>
    </defs>
    <circle class="back-bg" cx="410" cy="410" r="408" fill="var(--white)" stroke="var(--outline)" stroke-width="2"/>

    <text class="ring-text dark"><textPath href="#ring-path" startOffset="12.5%" text-anchor="middle">Hauskrankenpflege</textPath></text>
    <text class="ring-text blue"><textPath href="#ring-path" startOffset="37.5%" text-anchor="middle">Hauskrankenpflege</textPath></text>
    <text class="ring-text dark"><textPath href="#ring-path" startOffset="62.5%" text-anchor="middle">Hauskrankenpflege</textPath></text>
    <text class="ring-text blue"><textPath href="#ring-path" startOffset="87.5%" text-anchor="middle">Hauskrankenpflege</textPath></text>

    <g class="ring-dots" fill="var(--navy)">
      <circle cx="410" cy="53" r="7"/>
      <circle cx="767" cy="410" r="7"/>
      <circle cx="410" cy="767" r="7"/>
      <circle cx="53" cy="410" r="7"/>
    </g>

    <g class="back-mark">
      <circle cx="410" cy="410" r="212" fill="none" stroke="var(--blue)" stroke-width="20"/>
      <text class="mark-name-blue" x="410" y="402" text-anchor="middle" font-size="52">Sorgenhaus</text>
      <text class="mark-name-blue" x="410" y="462" text-anchor="middle" font-size="52">Linde</text>
    </g>
  </svg>

</main>
</body>
</html>
```